Postcard Design For House buying

I buy houses for cash that need a lot of repairs and need a post card that illustrate that, i would like one that is somehow cartoonish, I had an idea about a house and a man that was kicking to the house like you do with old cars and then he had some $ bills in his hand. This is just an idea and you should not limit yourself to that

Target Market(s)

Dallas TX (DFW)

Industry/Entity Type

Real Estate

Requirements
Must have
• A Text on the frot calling for action, like "Sell your house fast Call 512-374-9160"

```html
<!DOCTYPE html>
<html lang="en">
<head>
<meta charset="utf-8">
<title>Sell Your House Postcard</title>
<link rel="stylesheet" href="https://fonts.googleapis.com/css2?family=Fredoka:wght@600&family=Alfa+Slab+One&family=Nunito:wght@600&family=Open+Sans:wght@700&display=swap">
<style>
  :root {
    --page: #ffffff;
    --page-border: #3a3a3a;
    --orange-deep: #ff6f14;
    --orange-mid: #ff8c1e;
    --sun-yellow: #ffc61a;
    --card-edge: #ff9a10;
    --grass-light: #8fe048;
    --grass-dark: #3fa61c;
    --white: #ffffff;
    --heading-dark: #2a1506;
    --badge-yellow: #ffc805;
    --ink: #111111;
    --art-blue: #1b4fae;
    --art-green: #7cc43a;
  }
  * { margin: 0; padding: 0; box-sizing: border-box; }
  html, body { width: 1200px; height: 1200px; overflow: hidden; background: var(--page); }
  .page {
    position: relative; width: 1200px; height: 1200px;
    border: 2px solid var(--page-border); background: var(--page);
  }
  .postcard {
    position: absolute; left: 27px; top: 287px; width: 1145px; height: 624px;
    overflow: hidden;
    background:
      radial-gradient(circle at 92% 12%, rgba(255,240,150,0.85) 0, rgba(255,210,60,0.6) 18%, rgba(255,190,30,0) 45%),
      linear-gradient(90deg, var(--orange-deep) 0%, var(--orange-mid) 45%, var(--sun-yellow) 100%);
    box-shadow: inset 0 0 0 8px var(--card-edge);
  }
  .hill { position: absolute; left: 0; top: 400px; width: 1145px; height: 224px; }
  .headline {
    position: absolute; left: 72px; top: 30px;
    font-family: "Fredoka", sans-serif; font-weight: 600;
    font-size: 58px; line-height: 64px; color: var(--white); letter-spacing: 1px;
  }
  .services-title {
    position: absolute; left: 78px; top: 230px;
    font-family: "Alfa Slab One", serif; font-size: 31px; color: var(--heading-dark);
    letter-spacing: 1px;
  }
  .services {
    position: absolute; left: 90px; top: 280px; list-style: none;
    font-family: "Nunito", sans-serif; font-weight: 600; font-size: 25px;
    line-height: 35px; color: var(--white);
  }
  .services li::before { content: "\2022"; margin-right: 5px; }
  .illustration {
    position: absolute; left: 540px; top: 100px; width: 511px; height: 368px;
    border-radius: 8px;
    background: linear-gradient(90deg, rgba(140,140,150,0.55) 0%, rgba(124,196,58,0.55) 60%, rgba(27,79,174,0.5) 100%);
  }
  .badge {
    position: absolute; left: 50px; top: 442px; width: 170px; height: 170px;
    border-radius: 50%; background: var(--badge-yellow); z-index: 2;
  }
  .cta {
    position: absolute; left: 203px; top: 485px; width: 615px; height: 84px;
    border-radius: 42px; background: var(--white);
    display: flex; align-items: center; padding-left: 42px;
    font-family: "Open Sans", sans-serif; font-weight: 700; font-size: 41px; color: var(--ink);
    z-index: 1;
  }
</style>
</head>
<body>
  <div class="page">
    <section class="postcard">
      <svg class="hill" viewBox="0 0 1145 224" preserveAspectRatio="none" aria-hidden="true">
        <defs>
          <linearGradient id="grassFill" x1="0" y1="0" x2="0" y2="1">
            <stop offset="0" stop-color="var(--grass-light)"/>
            <stop offset="1" stop-color="var(--grass-dark)"/>
          </linearGradient>
        </defs>
        <path d="M0 80 Q 300 40 600 28 Q 900 14 1145 12 L1145 224 L0 224 Z" fill="url(#grassFill)"/>
      </svg>

      <h1 class="headline">SELL<br>YOUR<br>HOUSE !!!</h1>

      <h2 class="services-title">WE HELP WITH :</h2>
      <ul class="services">
        <li>High Price</li>
        <li>Fast Process</li>
        <li>Understanding Selling &amp; Buying</li>
        <li>Guaranteed</li>
      </ul>

      <div class="illustration" role="img" aria-label="Cartoon businessman in a grey suit kicking a small green house with a blue roof while dollar bills fly around"></div>

      <div class="badge" aria-hidden="true"></div>
      <p class="cta">Fast Call 512-374-9160</p>
    </section>
  </div>
</body>
</html>
```